Yoga site design

we need to design a homepage and content sections for our yoga portal

Verandel

Verandel is a yoga community ecosystem dedicated to the yoga enthusiasts and adopters of an active lifestyle based upon yoga and ayurvedic living. The objective of Verandel is to expand the involvment and adoption of yoga across the communities and facilitate the profitable growth of the various stakeholders and service providers involved with the ecosystem

Site descriptor

The site will have 4 building blocks/functionalities as specified below;

1.Directory functionality wherein it would list yoga classes/events/ workshop/ retreats and show calendar by dates and place
1. when
2. where
3. what
4. who
5. cost
6. durations

2.Search functionality

a.Find a yoga class/studio close to you (location tagging/google maps)
search/show by studioname/ teacher/ Private sessions/ yoga family
1. when
2. where
3. what
4. who
5. cost

3.Content publishing capabilty

a.Micro sites studio directory/ teachers/ frequent event holders/ therapists - contributors and serviceproviders
1. words of descriprion about yourself and your business
2. an email address
3. a live web link
4. google maps
5. contact phone number
6. a logo upload
7. a picture of themselves, (we need to specify size)
8 Weekly/monthly calendar - where thay are and when

b.Topical content
• columns written by a refference or celebrity
• parts in Montly newsletter and/or downloadable

c.Monthly Newsletter

d.What is New/News/Flash Happenings on the Site

e.Community Board
a virtual meeting place on a login and username basis
• Chirper
• chat
• yoganetwork - offline community build
• find a group close to you!

4.E-commerce capability (Yoga store)
by category;
• yoga props
• yoga clothes
• Ayurvedic related products
• Books/Music/dvd
• skin/body
tickets to events -
Updates

Reason: not enough iterations

Reason: i was unwell for the last two weeks

Target Market(s)

yoga enthusiasts across multiple cities in europe and americas

Industry/Entity Type

Building

Requirements
Must have
• the design should not be intrusive and allow for multiple city instances to be created using the same deisgn sensibilities
Should not have
• i do not need any tech coding.

```html
<!DOCTYPE html>
<html lang="en">
<head>
<meta charset="utf-8">
<title>Verandel – Yoga Community</title>
<link href="https://fonts.googleapis.com/css2?family=Arimo:ital,wght@0,400;0,700;1,700&family=Open+Sans:wght@300&display=swap" rel="stylesheet">
<style>
  :root {
    --header-top: #0f4f0a;
    --header-bottom: #6ba52f;
    --band-dark: #3a3533;
    --band-mid: #4a4542;
    --highlight: #27cf2c;
    --cream-top: #f1f6d6;
    --cream-bottom: #edf1dd;
    --green-text: #1d6a10;
    --heading-green: #1a6510;
    --footer-warm: #f4ebc4;
    --footer-link: #bdb7b0;
    --photo-light: #9ccf5a;
    --photo-deep: #5e9d24;
    --white: #ffffff;
  }
  * { margin: 0; padding: 0; box-sizing: border-box; }
  html, body { width: 800px; height: 1200px; overflow: hidden; }
  body { font-family: "Arimo", Arial, sans-serif; background: var(--cream-bottom); position: relative; }

  .site-header {
    position: absolute; left: 0; top: 0; width: 800px; height: 163px;
    background: linear-gradient(to bottom, var(--header-top), var(--header-bottom));
    display: flex; align-items: center; justify-content: center; gap: 16px;
  }
  .brand-dot { width: 40px; height: 40px; border-radius: 50%; background: #cfe3bf; }
  .brand-name { font-size: 50px; font-weight: 700; color: var(--white); letter-spacing: 0.5px; }

  .hero {
    position: absolute; left: 0; top: 163px; width: 800px; height: 318px;
    background: radial-gradient(ellipse at 50% 40%, var(--band-mid), var(--band-dark));
  }
  .hero-intro {
    position: absolute; left: 35px; top: 80px; width: 260px;
    font-size: 15.6px; font-weight: 700; font-style: italic; line-height: 32px; color: var(--white);
  }
  .hero-intro em { color: var(--highlight); }
  .hero-photo {
    position: absolute; left: 308px; top: 24px; width: 479px; height: 268px;
    border: 7px solid var(--white);
    background: linear-gradient(135deg, var(--photo-light), var(--photo-deep));
  }

  .content {
    position: absolute; left: 0; top: 481px; width: 800px; height: 562px;
    background: linear-gradient(to bottom, var(--cream-top), var(--cream-bottom));
    color: var(--green-text);
  }
  .welcome-title { position: absolute; left: 59px; top: 36px; font-size: 29px; font-weight: 700; color: var(--heading-green); }
  .welcome-text { position: absolute; left: 60px; top: 91px; width: 682px; font-size: 16.6px; line-height: 26.67px; }
  .services-title { position: absolute; left: 60px; top: 333px; font-size: 21px; font-weight: 700; color: var(--heading-green); }
  .services-list { position: absolute; left: 66px; top: 372px; list-style: none; font-size: 16.6px; line-height: 20px; }
  .services-list li { height: 38.7px; }
  .services-list li::before { content: "▪ "; }

  .site-footer {
    position: absolute; left: 0; top: 1043px; width: 800px; height: 157px;
    background: radial-gradient(ellipse at 50% 40%, var(--band-mid), var(--band-dark));
  }
  .footer-phone { position: absolute; left: 31px; top: 27px; font-size: 19px; font-weight: 700; color: var(--footer-warm); }
  .footer-email { position: absolute; right: 16px; top: 27px; font-size: 19px; color: var(--footer-warm); }
  .footer-social { position: absolute; left: 32px; top: 75px; display: flex; gap: 18px; font-size: 14px; color: var(--footer-link); }
  .footer-social span { display: flex; align-items: center; gap: 6px; }
  .footer-social i { width: 20px; height: 20px; background: #8c8680; display: inline-block; }
  .footer-nav { position: absolute; right: 16px; top: 75px; font-family: "Open Sans", Arial, sans-serif; font-weight: 300; font-size: 18px; color: var(--footer-link); display: flex; gap: 18px; }
</style>
</head>
<body>
  <header class="site-header">
    <span class="brand-dot"></span>
    <span class="brand-name">Verandel</span>
  </header>

  <section class="hero">
    <p class="hero-intro">Verandel is a <em>yoga community</em> ecosystem dedicated to the yoga enthusiasts and adopters of an active lifestyle based upon <em>yoga and ayurvedic</em> living.</p>
    <div class="hero-photo" role="img" aria-label="Photo of hands in a meditation pose outdoors on green grass"></div>
  </section>

  <main class="content">
    <h1 class="welcome-title">Welcome to Verandel</h1>
    <p class="welcome-text">Lorem ipsum dolor sit amet, consectetur adipiscing elit. Praesent eget ipsum quam, et cursus justo. Pellentesque accumsan ultrices viverra. Cras mi elit, sollicitudin non convallis in, placerat non risus. In ut mauris vitae enim dignissim adipiscing. Aenean ac tellus lectus. Praesent faucibus mi id nisl congue sodales. Etiam scelerisque, lorem id ullamcorper elementum, nisl ipsum rutrum eros, sit amet vestibulum odio lorem eu lacus. Quisque tortor lectus, faucibus nec iaculis vel, eleifend vitae sem. In sodales sollicitudin sapien, at aliquet risus rutrum nec. Morbi dapibus vulputate mattis.</p>
    <h2 class="services-title">Our Services....</h2>
    <ul class="services-list">
      <li>Lorem ipsum dolor sit amet, consectetur adipiscing elit.</li>
      <li>Lorem ipsum dolor sit amet, consectetur adipiscing elit.</li>
      <li>Lorem ipsum dolor sit amet, consectetur adipiscing elit.</li>
      <li>Lorem ipsum dolor sit amet, consectetur adipiscing elit.</li>
      <li>Lorem ipsum dolor sit amet, consectetur adipiscing elit.</li>
    </ul>
  </main>

  <footer class="site-footer">
    <p class="footer-phone">Call us : +123 555 0190</p>
    <p class="footer-email">Email Address : hello@verandel.example</p>
    <div class="footer-social">
      <span><i></i>Friendly</span>
      <span><i></i>Chirper</span>
    </div>
    <nav class="footer-nav">
      <span>Home</span><span>I</span><span>Newletter</span><span>I</span><span>Contact us</span>
    </nav>
  </footer>
</body>
</html>
```